Business Card Design

I want a business card with houses on the left hand side with pictures of young, middle age and a family in each house. I want the outline of the house to be dark blue and the background of the card to be pale blue. On the back of the card we want "We Love Referrals" on it with the company name and phone number. We are a real estate company who sells residential houses.

Industry/Entity Type

Real Estate

Contact Information for Business Card

Tolbert Harbour Properties
Dennis Varkoulatis
Exective Consultant
47 Brevanti Close
Wyndle Vale NSW 2718
Phone: 9514-7302
Mobile: 0427 381 645
Email: dennis@tolbertrealty.com.au

```html
<!DOCTYPE html>
<html lang="en">
<head>
<meta charset="utf-8">
<title>Tolbert Harbour Properties — Card Back</title>
<link rel="stylesheet" href="https://fonts.googleapis.com/css2?family=Arimo:wght@400;700&display=swap">
<style>
  :root {
    --card-bg: #b8edfc;
    --navy: #000874;
    --white: #ffffff;
  }
  html, body {
    margin: 0;
    padding: 0;
    width: 1200px;
    height: 741px;
    overflow: hidden;
    background: var(--card-bg);
  }
  .card {
    position: relative;
    width: 1200px;
    height: 741px;
    background: var(--card-bg);
    font-family: "Arimo", "Helvetica Neue", Arial, sans-serif;
    color: var(--navy);
  }
  .company-name {
    position: absolute;
    top: 263px;
    left: 0;
    width: 1200px;
    margin: 0;
    text-align: center;
    font-weight: 400;
    font-size: 72px;
    letter-spacing: -0.5px;
    line-height: 72px;
    white-space: nowrap;
  }
  .tagline {
    position: absolute;
    top: 357px;
    left: 0;
    width: 1200px;
    margin: 0;
    text-align: center;
    font-weight: 400;
    font-size: 37px;
    line-height: 43px;
  }
  .referral-band {
    position: absolute;
    top: 558px;
    left: 0;
    width: 1200px;
    height: 53px;
    background: var(--navy);
    color: var(--white);
    display: flex;
    align-items: center;
    justify-content: center;
    font-weight: 700;
    font-size: 31px;
    line-height: 1;
  }
  .contact-line {
    position: absolute;
    top: 645px;
    left: 0;
    width: 1200px;
    margin: 0;
    text-align: center;
    font-weight: 400;
    font-size: 28px;
    line-height: 34px;
  }
  .contact-line .label {
    font-weight: 700;
  }
  .contact-line .divider {
    display: inline-block;
    margin: 0 18px;
  }
</style>
</head>
<body>
  <main class="card">
    <h1 class="company-name">Tolbert Harbour Properties</h1>
    <p class="tagline">We are a real estate company who<br>sells residential houses.</p>
    <div class="referral-band">We Love Referrals</div>
    <p class="contact-line"><span class="label">Phone</span> 9514-7302<span class="divider">|</span><span class="label">Mobile</span> 0427 381 645</p>
  </main>
</body>
</html>
```